We need a quick postcard to mail out to our alumni telling them that they are invited to vote on a new ballot of alumni officers. I purchased a 4 color picture I want to use for the front of the postcard from pixmart but I can't get it to upload. Someone can email me at Marta.finch@bvrcampus.edu and I will email them the image. The final design needs to be clean and easy to read.

Offering doctoral, master’s, baccalaureate, and associate degrees, Saint Brigid of the Vale Campus is a four-year, independent Catholic institution, providing a strong foundation in the liberal arts and continuing its highly-regarded health sciences and nursing programs.

```html
<!DOCTYPE html>
<html lang="en">
<head>
<meta charset="utf-8">
<title>Alumni Vote Postcard</title>
<link href="https://fonts.googleapis.com/css2?family=Black+Ops+One&family=Marcellus+SC&family=Open+Sans:wght@400;600;700;800&display=swap" rel="stylesheet">
<style>
  :root {
    --page: #e9eaec;
    --card: #ffffff;
    --navy: #14294f;
    --navy-deep: #0d1c3a;
    --blue: #2f6fb3;
    --sky: #5aa3dc;
    --band: #4f9bd6;
    --ink: #2b2b2b;
    --link: #7cc4f2;
    --key-dark: #2a2c30;
    --key-mid: #5b5f66;
    --line: #222;
  }
  * { margin: 0; padding: 0; box-sizing: border-box; }
  html, body { width: 902px; height: 1200px; overflow: hidden; }
  body { background: var(--page); position: relative; font-family: "Open Sans", sans-serif; }

  .postcard {
    position: absolute; left: 112px; width: 678px; height: 525px;
    background: var(--card); overflow: hidden;
    box-shadow: 0 2px 8px rgba(0,0,0,.18);
  }
  .postcard--front { top: 40px; }
  .postcard--back { top: 620px; }

  /* front */
  .front-photo {
    position: absolute; left: 0; top: 0; width: 678px; height: 525px;
    background:
      radial-gradient(ellipse 150px 110px at 430px 230px, var(--sky) 0%, var(--blue) 55%, transparent 72%),
      linear-gradient(160deg, var(--key-mid) 0%, var(--key-dark) 45%, #44474d 75%, #8c9096 100%);
  }
  .front-swoosh { position: absolute; left: 0; top: 0; }
  .front-heading { position: absolute; left: 58px; top: 395px; }
  .front-heading__kicker {
    font-family: "Open Sans", sans-serif; font-weight: 800; font-size: 40px;
    color: var(--ink); line-height: 1; letter-spacing: -0.5px;
  }
  .front-heading__title {
    font-family: "Marcellus SC", serif; font-size: 48px; color: var(--navy);
    line-height: 1; margin-top: 14px; letter-spacing: 1px;
  }

  /* back */
  .back-panel { position: absolute; left: 0; top: 0; }
  .back-message {
    position: absolute; left: 28px; top: 36px; width: 268px;
    font-family: "Black Ops One", sans-serif; font-size: 14.5px; line-height: 26px;
    color: #fff;
  }
  .college-name {
    position: absolute; left: 58px; top: 222px; width: 230px;
    display: flex; align-items: center; gap: 12px;
  }
  .college-name__mark { width: 34px; height: 34px; background: #fff; flex: none; }
  .college-name__text {
    font-family: "Open Sans", sans-serif; font-weight: 700; font-size: 19px;
    line-height: 23px; color: #fff;
  }
  .back-cta {
    position: absolute; left: 30px; top: 338px; width: 275px;
    font-size: 14px; line-height: 20px; color: #fff; font-weight: 600;
  }
  .back-cta__url { color: var(--link); font-weight: 700; }
  .back-band {
    position: absolute; left: 28px; top: 468px;
    font-family: "Black Ops One", sans-serif; font-size: 20px; line-height: 30px;
    color: #111; letter-spacing: 0.5px;
  }
  .stamp-box {
    position: absolute; left: 608px; top: 38px; width: 62px; height: 74px;
    border: 2px solid var(--line);
  }
  .address-line {
    position: absolute; left: 480px; width: 190px; height: 1px; background: var(--line);
  }
</style>
</head>
<body>

<section class="postcard postcard--front">
  <div class="front-photo" role="img" aria-label="Close-up photograph of a computer keyboard with a blue enter key labelled Vote"></div>
  <svg class="front-swoosh" width="678" height="525" viewBox="0 0 678 525">
    <path d="M0 365 C180 318 420 392 678 470 L678 525 L0 525 Z" fill="var(--navy)"/>
    <path d="M0 375 C180 332 420 400 678 482 L678 525 L0 525 Z" fill="var(--blue)"/>
    <path d="M0 382 C190 345 430 418 678 510 L678 525 L0 525 Z" fill="var(--card)"/>
  </svg>
  <div class="front-heading">
    <div class="front-heading__kicker">Alumni:</div>
    <div class="front-heading__title">Please Vote!</div>
  </div>
</section>

<section class="postcard postcard--back">
  <svg class="back-panel" width="420" height="525" viewBox="0 0 420 525">
    <defs>
      <radialGradient id="panelGlow" cx="0.45" cy="0.45" r="0.7">
        <stop offset="0" stop-color="#2c5a9a"/>
        <stop offset="1" stop-color="#10224a"/>
      </radialGradient>
    </defs>
    <path d="M0 0 L285 0 C395 120 405 360 300 525 L0 525 Z" fill="#111"/>
    <path d="M0 0 L270 0 C375 120 380 360 290 525 L0 525 Z" fill="#fff"/>
    <path d="M0 0 L262 0 C366 120 372 360 282 525 L0 525 Z" fill="url(#panelGlow)"/>
    <path d="M0 448 L336 448 C320 478 305 505 290 525 L0 525 Z" fill="var(--band)"/>
    <line x1="0" y1="448" x2="336" y2="448" stroke="#fff" stroke-width="2"/>
  </svg>

  <p class="back-message">Alumni Association Executive Committee has been working on a major revision to the Alumni Association bylaws. In order to confirm the new by laws we need your approval !</p>

  <div class="college-name">
    <span class="college-name__mark"></span>
    <span class="college-name__text">Saint Brigid of the Vale Campus</span>
  </div>

  <p class="back-cta">Go to <span class="back-cta__url">bvrcampus.edu/alumni-feedback</span> to give us your responses to the proposed bylaws and to vote on a new slate of officers.</p>

  <p class="back-band">WE VALUE YOUR OPINION<br>VOTE TODAY!</p>

  <div class="stamp-box"></div>
  <div class="address-line" style="top:295px"></div>
  <div class="address-line" style="top:335px"></div>
  <div class="address-line" style="top:375px"></div>
</section>

</body>
</html>
```